Brook Haven Yellow Perch Fish Stock and immune system boosts

We are a non-profit that sets up Aquaponics's systems in cities of 5000 or less in the Midwest. We have created a product that uses our yellow perch carcasses as the base for this broth. Our fish are grown in containment from egg to market size fish. This means it is the safest most sustainable product on the market. We also use veggies grown in the same aquaponics system network. One product has oriental overtones and mixed with antioxidants as a gut immune system bacteria booster. The other is a standard broth that has multiple uses. We are looking for packaging for both our broths. We have included our logo (a sketch hive creation). This product packaging will also be a media piece promoting The Brook Haven way of life and a way to raise revenue for the non-profit. We have not chosen the names of products but will be under the "Brook Haven" verbiage. Example is " "Brook Haven Minnow Might stock"
I have added some current examples of packaging

Target Market(s)

consumers and commercial clients

Industry/Entity Type

Grocery Store

Colors

Designer to choose colors to be used in the design.

Requirements
Must have
• Fresh feeling, restorative qualities, safe, sustainable
• Package size is 32 oz. shape is flexible

```html
<!DOCTYPE html>
<html lang="en">
<head>
<meta charset="utf-8">
<title>Brook Haven Minnow Might Stock – Packaging</title>
<link href="https://fonts.googleapis.com/css2?family=Arimo:ital,wght@0,400;0,700;1,700&family=Roboto+Condensed:wght@300;400;700&display=swap" rel="stylesheet">
<style>
  :root{
    --leaf:#9dc83b; --navy:#1e5b8e; --mint:#6cc4a4; --orange:#f0a030;
    --mustard:#e6c52a; --sky:#8bcbd8; --teal:#2e8a78; --ink:#231f20;
    --text:#555; --panel:#fff; --stage:#f3f3f3; --edge:#d9d9d9;
    --water-a:#d9ecc0; --water-b:#eef6e2;
  }
  *{box-sizing:border-box;margin:0;padding:0}
  html,body{width:1200px;height:526px;overflow:hidden}
  body{background:linear-gradient(#e6e6e6,var(--stage) 30%,#fff);font-family:"Arimo",sans-serif;color:var(--text);position:relative}
  .sheet{position:absolute;background:var(--panel);border:1px solid var(--edge);overflow:hidden}
  .dieline{left:55px;top:50px;width:464px;height:387px}
  .pouch-front{left:568px;top:50px;width:266px;height:398px}
  .pouch-back{left:864px;top:50px;width:266px;height:398px}
  .abs{position:absolute}
  .handle{top:30px;width:58px;height:17px;border-radius:7px;background:#d4d4d4;border:1px solid #bbb}
  .brand{display:flex;align-items:center;gap:4px;font-size:9px;font-weight:700;color:var(--navy);white-space:nowrap}
  .brand-dot{width:26px;height:26px;border-radius:50%;background:var(--leaf)}
  .tagline{font-style:italic;font-weight:700;font-size:8.6px;line-height:10px;color:var(--navy);text-align:right;width:120px}
  .about{font-size:6px;line-height:8px;letter-spacing:-.1px;color:#777}
  .about b{color:var(--navy)}
  .water{background:linear-gradient(90deg,var(--water-a),var(--water-b) 55%,#fff 78%);border-top:3px solid #cfe8ee}
  .water.full{background:linear-gradient(90deg,var(--water-a),var(--water-b) 70%,#f4f9ee)}
  .title{font-family:"Roboto Condensed",sans-serif;font-weight:300;font-size:29px;line-height:30px;color:var(--sky);letter-spacing:-.3px}
  .subtitle{font-family:"Roboto Condensed",sans-serif;font-weight:700;font-size:17px;line-height:18px;color:var(--leaf)}
  .photo{background:radial-gradient(ellipse at 50% 50%,#7d8a86,#b8c5b0 55%,rgba(220,236,200,0) 72%)}
  .boost-bar{height:16px;background:linear-gradient(90deg,var(--sky),rgba(139,203,216,.2));color:#fff;font-family:"Roboto Condensed",sans-serif;font-weight:700;font-size:10px;line-height:16px;padding-left:20px}
  .url{font-family:"Roboto Condensed",sans-serif;font-weight:700;font-size:7.5px;color:var(--sky);letter-spacing:.4px}
  .pattern{background:linear-gradient(#eef8fa,#d9eff3)}
  .mix h3{font-size:7px;font-weight:400;color:var(--ink);text-align:center;margin-bottom:2px}
  .mix .lead{font-size:6.2px;color:var(--ink);margin-bottom:5px}
  .mix ol{list-style:none}
  .mix li{position:relative;padding-left:12px;font-size:6.2px;line-height:7.6px;color:var(--ink);margin-bottom:5px}
  .mix li span{position:absolute;left:0;top:0;width:8px;height:8px;border-radius:50%;background:var(--sky);color:#fff;font-size:5.5px;line-height:8px;text-align:center}
  .legal{font-size:5px;line-height:6.2px;color:var(--ink);text-align:center}
  .social{font-size:5.4px;line-height:8px;color:var(--ink)}
  .recycle{display:flex;flex-direction:column;align-items:center;font-size:4.6px;color:var(--navy)}
  .recycle i{display:block;width:18px;height:18px;border-radius:50%;border:2px solid var(--navy);margin-bottom:2px}
  .size{font-weight:700;font-size:8.5px;line-height:10px;color:var(--navy)}
  .swatches{position:absolute;left:61px;top:458px;display:flex;gap:5px}
  .swatch{width:22px;height:22px}
  .swatch-label{position:absolute;left:282px;top:466px;font-size:6.5px;color:var(--ink)}
</style>
</head>
<body>

<section class="sheet dieline">
  <div class="abs handle" style="left:87px"></div>
  <div class="abs handle" style="left:318px"></div>

  <div class="abs brand" style="left:22px;top:80px"><span class="brand-dot"></span>Brook Haven</div>
  <p class="abs tagline" style="left:114px;top:78px">YELLOW PERCH<br>BASED FISH BROTH<br>WITH RESTORATIVE<br>PROPERTIES</p>

  <div class="abs brand" style="left:260px;top:80px"><span class="brand-dot"></span></div>
  <p class="abs about" style="left:312px;top:68px;width:146px"><b>BROOK HAVEN</b> is a non-profit company specializing in Aquaponics, growing of fish to produce vegetables and fish based products. This both is made from Yellow perch has restorative properties, high in protein and other essential vitamins and minerals a great immune system boost broth.</p>

  <div class="abs water" style="left:0;top:128px;width:464px;height:214px"></div>
  <div class="abs photo" role="img" aria-label="Yellow perch swimming among green water plants" style="left:120px;top:150px;width:150px;height:180px"></div>
  <h1 class="abs title" style="left:21px;top:148px">BROOK HAVEN</h1>
  <h2 class="abs subtitle" style="left:21px;top:182px">MINNOW MIGHT STOCK</h2>
  <div class="abs boost-bar" style="left:0;top:302px;width:240px">IMMUNE SYSTEM BOOST</div>

  <div class="abs mix" style="left:268px;top:172px;width:150px">
    <h3>Mixing Instructions</h3>
    <p class="lead">For best results:</p>
    <ol>
      <li><span>1</span>Lorem ipsum dolor sit amet, sed quod diam diceret ne. Delenit noluisse elaboraret per no, viderer.</li>
      <li><span>2</span>Officiis assueverit te mea. Cu elit vocent expetendis quo. Elitr clita quidam ut mei, nemore contentiones pri an. Ad vim detraxit suscipiantur interpretaris.</li>
      <li><span>3</span>At pro recusabo vituperata sadipscing, detracto consequat nec ne. Electram consectetuer vix et, per in alienum senserit.</li>
    </ol>
  </div>
  <p class="abs legal" style="left:265px;top:288px;width:160px">Brook Haven products are produced exclusively for brookhaven.org by Brook Haven Great Lakes Ltd</p>
  <p class="abs social" style="left:290px;top:308px">www.brookhaven.org/community<br>@brookhaven</p>
  <div class="abs recycle" style="left:398px;top:300px"><i></i>RECYCLE</div>
  <p class="abs size" style="left:397px;top:328px">32oz</p>

  <p class="abs url" style="left:78px;top:346px">WWW.BROOKHAVEN.ORG</p>
  <p class="abs url" style="left:315px;top:346px">WWW.BROOKHAVEN.ORG</p>
  <div class="abs pattern" role="img" aria-label="Light blue fish outline pattern band" style="left:0;top:358px;width:464px;height:29px"></div>
</section>

<section class="sheet pouch-front">
  <div class="abs brand" style="left:22px;top:80px"><span class="brand-dot"></span>Brook Haven</div>
  <p class="abs tagline" style="left:110px;top:78px">YELLOW PERCH<br>BASED FISH BROTH<br>WITH RESTORATIVE<br>PROPERTIES</p>
  <div class="abs water full" style="left:0;top:127px;width:266px;height:200px"></div>
  <div class="abs photo" role="img" aria-label="Yellow perch swimming among green water plants" style="left:120px;top:150px;width:140px;height:175px"></div>
  <h1 class="abs title" style="left:22px;top:148px">BROOK HAVEN</h1>
  <h2 class="abs subtitle" style="left:22px;top:182px">MINNOW MIGHT STOCK</h2>
  <div class="abs boost-bar" style="left:0;top:302px;width:200px">IMMUNE SYSTEM BOOST</div>
  <p class="abs url" style="left:80px;top:343px">WWW.BROOKHAVEN.ORG</p>
  <div class="abs pattern" role="img" aria-label="Light blue fish outline pattern band" style="left:0;top:356px;width:266px;height:30px"></div>
</section>

<section class="sheet pouch-back">
  <div class="abs brand" style="left:40px;top:84px"><span class="brand-dot"></span></div>
  <p class="abs about" style="left:96px;top:84px;width:162px;font-size:6.4px;line-height:8.4px"><b>BROOK HAVEN</b> is a non-profit company specializing in Aquaponics, growing of fish to produce vegetables and fish based products. This both is made from Yellow perch has restorative properties, high in protein and other essential vitamins and minerals a great immune system boost broth.</p>
  <div class="abs water" style="left:0;top:146px;width:266px;height:40px"></div>
  <div class="abs mix" style="left:48px;top:194px;width:170px">
    <h3>Mixing Instructions</h3>
    <p class="lead">For best results:</p>
    <ol>
      <li><span>1</span>Lorem ipsum dolor sit amet, sed quod diam diceret ne. Delenit noluisse elaboraret per no, viderer.</li>
      <li><span>2</span>Officiis assueverit te mea. Cu elit vocent expetendis quo. Elitr clita quidam ut mei, nemore contentiones pri an. Ad vim detraxit suscipiantur interpretaris.</li>
      <li><span>3</span>At pro recusabo vituperata sadipscing, detracto consequat nec ne. Electram consectetuer vix et, per in alienum senserit.</li>
    </ol>
  </div>
  <p class="abs legal" style="left:50px;top:314px;width:166px">Brook Haven products are produced exclusively for brookhaven.org by Brook Haven Great Lakes Ltd</p>
  <p class="abs social" style="left:74px;top:330px">www.brookhaven.org/community<br>@brookhaven</p>
  <div class="abs recycle" style="left:196px;top:326px"><i></i>RECYCLE</div>
  <p class="abs size" style="left:196px;top:356px">32oz</p>
  <p class="abs url" style="left:90px;top:372px">WWW.BROOKHAVEN.ORG</p>
</section>

<div class="swatches">
  <span class="swatch" style="background:var(--leaf)"></span>
  <span class="swatch" style="background:var(--navy)"></span>
  <span class="swatch" style="background:var(--mint)"></span>
  <span class="swatch" style="background:var(--orange)"></span>
  <span class="swatch" style="background:var(--mustard)"></span>
  <span class="swatch" style="background:var(--sky)"></span>
  <span class="swatch" style="background:var(--teal)"></span>
  <span class="swatch" style="background:var(--ink)"></span>
</div>
<p class="swatch-label">Brook Haven colour BRAND</p>

</body>
</html>
```